2-Page Flyer for the Information Session about the Tranquil Venture Course

This is a flyer to announce/advertise an evening Information Session about the Tranquil Venture Course. This Program aims at mindfully rethinking and redesigning work (and life) for people who feel stuck or not entirely satisfied with their work and/or life (please see draft flyer attached for more details). This Program is property of Brightfold Joy, a company that uses a combination of Mindfulness, Design, and Entrepreneurship to help people achieve greater happiness (in their work and lives).
Updates

Target Market(s)

People who feel stuck or not entirely satisfied with their work and/or life (please see draft flyer attached for more details)

Font styles to use
Serif
Sans Serif

Colors
ffffff
f37122
33a6d7
acd037

Requirements
Must have
• All of what I will say below is suggestive (I’m not a design expert), and I’m open to divert from it, if it makes sense and feels more interesting.
• I thought initially of a 2-page flyer (please see draft flyer attached). The first page could help people grasp the essence of the event quickly (in 1 or 2 minutes), and then, if they are interested/motivated, they would continue reading through page 2, which has more info about the Program in itself.
• Potential Structure
• Page 1
• . About the Information Session on the Tranquil Venture Course
• . Visible Date & Time, Contacts, Venue (and other relevant info)
• . About me (the facilitator)
• Page 2
• . About the Tranquil Venture Course
• I include a Powerpoint draft of the flyer with the content. The design is rudimentary and precarious from an aesthetics/organization point of view, and this is mainly where I need help (and maybe in other aspects too!).
• On the flyer, I would like to include:
• . A photo of myself (I attach 1 picture).
• . 1 or 2 beautiful-nature photos (cropped or full). One may have to do with looking at the sky, dreaming, and imagining a new work and life (2 photos with sky and clouds attached). The other has to do with walking the transformation journey (the photo with the person walking through the forest path).
• . brightfold joy logo or logos (there are two slightly different ones, that can be used for different purposes). For the first page, I would like the brightfold joy logo that has "brightfold joy" written on the bottom, with the saying "Stillness, Craft and Venture for Joy" beneath. This is the main logo. For the 2nd page, you can choose the logo that adapts better.
• - Where it says the "the way out is in" it would be great to have a similar font to the one I attach (see file "Font_the_way_out_is_in.png" and Ankecallig-fg.ttf
Nice to have
• In terms of colours, I would not divert much from the logo colours (and of course white and black). I would like the flyer to be quite white. Almost like fairy-tale white: the white horse, the white snow, the white of the stars, the white heaven. White could be the base colour. White means peace, tranquillity, calm contentment, a smile.
• And then use the other colours. The green of the mindfulness. The blue of the sky, the dreams. And the orange of the sun, the energy, the fire, the action. And maybe the black for text.
• Where it says the "the way out is in" it would be great to have a similar font to the one I attach (see file "Font_the_way_out_is_in".
• I would like this flyer to be a piece of art, in every possible way. Simple, beautiful, ease, light, peaceful, calm happy. Just like the Tranquil Venture Course and brightfold joy Company that I am creating intends to be. The mission of this Program and Company is to be a designer, a painter (a Picasso) of happier and more fulfilling human lives.
• I am very much looking forward to seeing your proposal(s).

```html
<!DOCTYPE html>
<html lang="en">
<head>
<meta charset="utf-8">
<title>Tranquil Venture Course – Information Session Flyer</title>
<link href="https://fonts.googleapis.com/css2?family=Montserrat:wght@600;700;800&family=Open+Sans:wght@400;600;700&family=Homemade+Apple&display=swap" rel="stylesheet">
<style>
  :root{
    --white:#ffffff;
    --orange:#f37122;
    --blue:#33a6d7;
    --green:#acd037;
    --ink:#2b2b2b;
    --muted:#5b5b5b;
    --panel:#eef2f4;
    --stage:#e6e7e8;
  }
  *{box-sizing:border-box;margin:0;padding:0}
  html,body{width:700px;height:1200px;overflow:hidden}
  body{background:var(--stage);font-family:"Open Sans",Arial,sans-serif;color:var(--ink);position:relative}
  .page{position:absolute;left:145px;width:410px;height:580px;background:var(--white);box-shadow:0 2px 8px rgba(0,0,0,.18);overflow:hidden}
  .page--front{top:10px}
  .page--back{top:610px}
  .abs{position:absolute}
  p{font-size:6.6px;line-height:1.45;color:var(--muted)}
  h3{font-family:"Montserrat",Arial,sans-serif;font-weight:700;font-size:10px}
  .brand{left:18px;top:18px;width:96px}
  .brand__row{display:flex;align-items:center;gap:5px}
  .brand__dot{width:16px;height:16px;border-radius:50%;background:var(--blue)}
  .brand__name{font-family:"Open Sans",sans-serif;font-weight:700;font-size:12px;color:var(--orange)}
  .brand__tag{font-size:5px;color:var(--muted);margin-top:3px;line-height:1.3}
  .title{left:125px;top:18px;width:270px;font-family:"Montserrat",Arial,sans-serif;font-weight:800;font-size:25px;line-height:1.02;color:var(--ink);text-transform:uppercase;letter-spacing:-.3px}
  .rule{left:18px;right:18px;top:90px;height:2px;background:var(--blue)}
  .session{left:18px;top:102px;width:92px}
  .session__label{font-family:"Montserrat",sans-serif;font-weight:800;font-size:11px;line-height:1.1;color:var(--orange);text-transform:uppercase}
  .session__item{margin-top:8px;font-size:7px;line-height:1.35;font-weight:600;color:var(--ink)}
  .session__item span{display:block;font-weight:400;color:var(--muted)}
  .intro{left:125px;top:102px;width:268px}
  .intro .lead{font-weight:700;color:var(--ink);font-size:7.2px}
  .intro h3{color:var(--blue);margin:8px 0 3px}
  .about{left:0;top:240px;width:410px;height:225px;background:var(--panel)}
  .about__text{left:18px;top:14px;width:225px}
  .about__text h3{color:var(--orange);margin-bottom:4px}
  .about__text .name{font-weight:700;color:var(--ink);font-size:7px;margin-bottom:3px}
  .portrait{left:255px;top:-18px;width:140px;height:243px;background:linear-gradient(180deg,#b9c3c9,#6f7d86 60%,#3a4249)}
  .more{left:18px;top:478px;width:180px;height:22px;background:var(--green);color:var(--white);font-size:7px;font-weight:700;display:flex;align-items:center;padding-left:8px}
  .forest{background:linear-gradient(160deg,#dfe8d6,#8fae7a 45%,#49643f)}
  .forest--front{left:210px;top:470px;width:200px;height:75px}
  .motto{font-family:"Homemade Apple",cursive;color:var(--white);font-size:12px;text-shadow:0 1px 2px rgba(0,0,0,.3)}
  .contact{left:0;bottom:0;width:410px;height:35px;display:flex;align-items:center;gap:14px;padding:0 18px;font-size:7px;color:var(--white)}
  .contact--front{background:var(--orange)}
  .contact--back{background:var(--blue)}
  .contact b{font-family:"Montserrat",sans-serif;font-size:8px}
  .contact__item{display:flex;align-items:center;gap:4px}
  .sky{left:0;top:0;width:410px;height:130px;background:linear-gradient(180deg,#7fbde0,#bfe0f1 60%,#eef6fb)}
  .headline{left:18px;top:20px;width:280px;background:var(--white);padding:10px 12px}
  .headline h2{font-family:"Montserrat",sans-serif;font-weight:800;font-size:14px;color:var(--blue);margin-bottom:5px}
  .col-left{left:18px;width:190px}
  .col-right{left:222px;width:170px}
  .sec h3{color:var(--orange);margin-bottom:4px}
  .sec--blue h3{color:var(--blue)}
  .sec p+p{margin-top:4px}
  .checks{list-style:none;margin-top:4px}
  .checks li{display:flex;gap:4px;font-size:6.6px;line-height:1.4;color:var(--muted);margin-bottom:3px}
  .checks svg{flex:0 0 8px;margin-top:1px}
  .forest--back{left:0;top:450px;width:410px;height:95px}
</style>
</head>
<body>

<section class="page page--front">
  <div class="abs brand">
    <div class="brand__row"><span class="brand__dot"></span><span class="brand__name">brightfold joy</span></div>
    <div class="brand__tag">Stillness, Craft and Venture for Joy</div>
  </div>
  <h1 class="abs title">Tranquil Venture Course</h1>
  <div class="abs rule"></div>

  <div class="abs session">
    <div class="session__label">Free Information Session</div>
    <div class="session__item">Thursday<span>28 September 2017</span></div>
    <div class="session__item">19:00 to 21:00</div>
    <div class="session__item">Linden Hall Studio<span>14 Orchard Lane</span></div>
  </div>

  <div class="abs intro">
    <p class="lead">The purpose of this free Information Session is to give you a real insight into the Tranquil Venture Course and how it can help you make the most of your professional and personal life.</p>
    <h3>Who Can Come</h3>
    <p>Whether you come to your own, or with friends or family, you'll be warmly welcomed. This session is for anyone who feels a little stuck or not fully content with their work or life, and who would like to explore a calmer, more meaningful way forward. No prior experience is needed. Please book your place in advance, as spaces are limited and we would love to prepare a seat for you.</p>
  </div>

  <div class="abs about">
    <div class="abs about__text">
      <h3>About Facilitator</h3>
      <p class="name">Tomas Arvel – Founder of Brightfold Joy</p>
      <p>Tomas has spent many years working across design, business and personal growth. After a long career in busy organisations, he began a deep practice of stillness that slowly changed how he saw work and life. Today he brings these threads together to help people rethink their path with curiosity and kindness.</p>
      <p style="margin-top:4px">He has guided groups and individuals through courses, retreats and one-to-one sessions, and believes that every person can shape a working life that feels lighter, truer and more joyful. His sessions are gentle, practical and open to all.</p>
    </div>
    <div class="abs portrait" role="img" aria-label="Portrait photo of the facilitator"></div>
  </div>

  <div class="abs more">More about the facilitator at brightfoldjoy.example</div>
  <div class="abs forest forest--front" role="img" aria-label="Photo of a person walking along a forest path">
    <span class="abs motto" style="right:10px;bottom:10px">the way out is in</span>
  </div>

  <div class="abs contact contact--front">
    <b>Information &amp; Booking</b>
    <span class="contact__item">
      <svg width="8" height="8" viewBox="0 0 24 24"><path fill="#fff" d="M6.6 10.8a15 15 0 0 0 6.6 6.6l2.2-2.2a1 1 0 0 1 1-.25 11.4 11.4 0 0 0 3.6.57 1 1 0 0 1 1 1V20a1 1 0 0 1-1 1A17 17 0 0 1 3 4a1 1 0 0 1 1-1h3.5a1 1 0 0 1 1 1c0 1.25.2 2.45.57 3.6a1 1 0 0 1-.25 1z"/></svg>
      +00 555 0142 880</span>
    <span class="contact__item">
      <svg width="9" height="7" viewBox="0 0 24 18"><rect x="1" y="1" width="22" height="16" fill="none" stroke="#fff" stroke-width="2"/><path d="M1 1l11 9 11-9" fill="none" stroke="#fff" stroke-width="2"/></svg>
      hello@brightfoldjoy.example</span>
  </div>
</section>

<section class="page page--back">
  <div class="abs sky" role="img" aria-label="Photo of a blue sky with soft clouds"></div>
  <div class="abs headline">
    <h2>What is Tranquil Venture</h2>
    <p>Tranquil Venture brings stillness, craft and venture together so you can pause, look inward and redesign your work and life with clarity, care and a sense of quiet courage.</p>
  </div>

  <div class="abs col-left sec" style="top:148px">
    <h3>The Program</h3>
    <p>The Tranquil Venture Course is a 6-week journey designed to help you step back from the rush of daily life, notice what really matters to you and shape a new direction with intention.</p>
    <p>Each week combines a short practice of stillness, creative design exercises and simple venture tools. You will reflect, imagine and test small steps, supported by a warm group of fellow travellers.</p>
  </div>

  <svg class="abs col-right" style="top:150px" width="170" height="120" viewBox="0 0 170 120" role="img" aria-label="Three circles: Stillness, Craft and Venture">
    <line x1="42" y1="40" x2="128" y2="40" stroke="#cfd6da" stroke-width="1.5"/>
    <line x1="42" y1="40" x2="85" y2="90" stroke="#cfd6da" stroke-width="1.5"/>
    <line x1="128" y1="40" x2="85" y2="90" stroke="#cfd6da" stroke-width="1.5"/>
    <circle cx="42" cy="40" r="26" fill="var(--green)"/>
    <circle cx="128" cy="40" r="26" fill="var(--blue)"/>
    <circle cx="85" cy="90" r="26" fill="var(--orange)"/>
    <g font-family="Montserrat, sans-serif" font-weight="700" font-size="7" fill="#fff" text-anchor="middle">
      <text x="42" y="43">Stillness</text>
      <text x="128" y="43">Craft</text>
      <text x="85" y="93">Venture</text>
    </g>
  </svg>

  <div class="abs col-left sec sec--blue" style="top:290px">
    <h3>Why</h3>
    <p>Many of us feel stuck, tired or unsure about our work. This course offers space to slow down and ask:</p>
    <ul class="checks">
      <li><svg width="8" height="8" viewBox="0 0 10 10"><path d="M1 5l3 3 5-6" fill="none" stroke="var(--green)" stroke-width="1.8"/></svg>What gives me energy and meaning?</li>
      <li><svg width="8" height="8" viewBox="0 0 10 10"><path d="M1 5l3 3 5-6" fill="none" stroke="var(--green)" stroke-width="1.8"/></svg>Which talents do I want to use more?</li>
      <li><svg width="8" height="8" viewBox="0 0 10 10"><path d="M1 5l3 3 5-6" fill="none" stroke="var(--green)" stroke-width="1.8"/></svg>How can I take a first gentle step?</li>
    </ul>
  </div>

  <div class="abs col-right sec" style="top:290px">
    <h3>How</h3>
    <p>The course differs from usual programs because it joins inner work with practical design. You will:</p>
    <ul class="checks">
      <li><svg width="8" height="8" viewBox="0 0 10 10"><path d="M1 5l3 3 5-6" fill="none" stroke="var(--orange)" stroke-width="1.8"/></svg>practise simple daily stillness</li>
      <li><svg width="8" height="8" viewBox="0 0 10 10"><path d="M1 5l3 3 5-6" fill="none" stroke="var(--orange)" stroke-width="1.8"/></svg>sketch and prototype new paths</li>
      <li><svg width="8" height="8" viewBox="0 0 10 10"><path d="M1 5l3 3 5-6" fill="none" stroke="var(--orange)" stroke-width="1.8"/></svg>test ideas with real feedback</li>
    </ul>
  </div>

  <div class="abs forest forest--back" role="img" aria-label="Photo of a sunlit forest path">
    <span class="abs motto" style="right:22px;bottom:28px;font-size:15px">the way out is in</span>
  </div>

  <div class="abs contact contact--back">
    <span class="contact__item">
      <svg width="8" height="8" viewBox="0 0 24 24"><path fill="#fff" d="M6.6 10.8a15 15 0 0 0 6.6 6.6l2.2-2.2a1 1 0 0 1 1-.25 11.4 11.4 0 0 0 3.6.57 1 1 0 0 1 1 1V20a1 1 0 0 1-1 1A17 17 0 0 1 3 4a1 1 0 0 1 1-1h3.5a1 1 0 0 1 1 1c0 1.25.2 2.45.57 3.6a1 1 0 0 1-.25 1z"/></svg>
      +00 555 0142 880</span>
    <span class="contact__item">
      <svg width="9" height="7" viewBox="0 0 24 18"><rect x="1" y="1" width="22" height="16" fill="none" stroke="#fff" stroke-width="2"/><path d="M1 1l11 9 11-9" fill="none" stroke="#fff" stroke-width="2"/></svg>
      hello@brightfoldjoy.example</span>
    <span class="contact__item">brightfoldjoy.example</span>
  </div>
</section>

</body>
</html>
```